Brand new website for global research and investment startup

We need a simple website, maybe 3 pages: landing page with business description, investment philosophy, team and contact info.
We have a logo already that can be incorporated. Please use the logo only, not the text
We like the color green, something along the lines of #3D6C32 as the main color.
We'd like to design the website with geometric shapes in gradations of the base color. The shapes should suggest "work in progress", "built to last (a long time)", "solidity" and "indestructibility". One idea floating in my head sees smaller features with icosahedron and dodecahedron shapes, and maybe larger structures like crystal lattices; but please feel free to be creative and imagine your own.

```html
<!DOCTYPE html>
<html lang="en">
<head>
<meta charset="utf-8">
<title>Halden Forum — Global research, independent perspective</title>
<link rel="stylesheet" href="https://fonts.googleapis.com/css2?family=Newsreader:ital,opsz,wght@0,6..72,300;0,6..72,400;1,6..72,300;1,6..72,400&family=Inter:wght@400;500;600&display=swap">
<style>
:root{
  --forest:#142a1c;
  --forest-2:#1b3524;
  --leaf:#3d6c32;
  --leaf-soft:#6f9a5f;
  --mint:#b9dca6;
  --mint-pale:#dfe6d6;
  --paper:#f3f0e8;
  --stone:#e8e8df;
  --ink:#14231a;
  --muted:#6d7569;
  --line-dark:rgba(185,220,166,.18);
  --line-light:rgba(20,35,26,.14);
  --serif:"Newsreader",Georgia,serif;
  --sans:"Inter",Helvetica,Arial,sans-serif;
}
*{box-sizing:border-box;margin:0;padding:0}
html,body{width:1200px;height:5213px;overflow:hidden}
body{font-family:var(--sans);color:var(--ink);background:var(--paper)}
section,header,footer{position:relative;width:1200px;overflow:hidden}
.abs{position:absolute}
em{font-style:italic;font-weight:300}
.label{font-size:7px;letter-spacing:.14em;text-transform:uppercase;font-weight:500}
.label-rule{display:flex;align-items:center;gap:10px}
.label-rule::after{content:"";width:40px;height:1px;background:currentColor;opacity:.4}
.serif{font-family:var(--serif);font-weight:400;letter-spacing:-.02em;line-height:1}

/* hero */
.hero{height:676px;background:radial-gradient(ellipse at 78% 45%,#2a4a32 0%,#1a3322 40%,var(--forest) 75%);color:#eef2ea}
.nav{position:absolute;top:0;left:0;width:1200px;height:58px;display:flex;align-items:center;padding:0 30px;border-bottom:1px solid var(--line-dark)}
.brand{display:flex;align-items:center;gap:8px;font-family:var(--serif);font-size:17px;line-height:.9}
.brand-dot{width:18px;height:18px;border-radius:50%;border:1.5px solid currentColor}
.brand small{display:block;font-size:10px;letter-spacing:.3em}
.nav-links{position:absolute;left:495px;display:flex;gap:38px;font-size:7.5px;letter-spacing:.14em;font-weight:500}
.nav-cta{position:absolute;right:30px;display:flex;gap:12px;align-items:center;font-size:7.5px;letter-spacing:.14em;font-weight:500}
.hero-art{position:absolute;left:670px;top:120px;width:480px;height:440px;background:radial-gradient(ellipse at 50% 45%,rgba(111,154,95,.45) 0%,rgba(61,108,50,.25) 45%,rgba(20,42,28,0) 75%)}
.hero-title{position:absolute;left:120px;top:205px;font-size:92px;line-height:.92}
.hero-title span{display:block}
.hero-title em{color:var(--mint)}
.hero-desc{position:absolute;left:120px;top:586px;width:270px;font-size:9px;line-height:1.7;color:#b5c2b0}
.hero-btn{position:absolute;left:985px;top:555px;width:96px;height:96px;border-radius:50%;background:var(--mint);color:var(--forest);display:flex;flex-direction:column;align-items:center;justify-content:center;font-size:6.5px;letter-spacing:.12em;font-weight:600;text-align:center;line-height:1.5;box-shadow:0 0 0 8px rgba(185,220,166,.15)}

/* forum */
.forum{height:721px;background:var(--paper)}
.big-head{font-size:62px;line-height:1.02}
.big-head em{color:var(--leaf)}
.link-line{display:flex;justify-content:space-between;align-items:center;border-bottom:1px solid var(--ink);padding-bottom:8px;font-size:7px;letter-spacing:.14em;font-weight:600}
.marquee{position:absolute;left:-30px;top:502px;white-space:nowrap;font-family:var(--serif);font-size:134px;color:#c3cbbd;letter-spacing:-.03em}
.marquee i{font-style:normal;font-family:var(--sans);font-size:34px;color:var(--leaf);margin:0 24px;vertical-align:middle}

/* perspectives */
.perspectives{height:1028px;background:var(--forest);color:#eef2ea}
.persp-head{font-size:64px;line-height:1}
.persp-head em{color:var(--mint)}
.persp-grid{position:absolute;left:120px;top:433px;width:960px;height:492px;border-top:1px solid var(--line-dark);display:grid;grid-template-columns:551px 409px}
.persp-visual{position:relative;border-right:1px solid var(--line-dark)}
.persp-art{position:absolute;left:100px;top:90px;width:350px;height:300px;background:radial-gradient(ellipse at 50% 50%,rgba(111,154,95,.4) 0%,rgba(61,108,50,.2) 50%,rgba(20,42,28,0) 75%);display:flex;align-items:center;justify-content:center;font-family:var(--serif);font-size:13px;color:#eef2ea}
.persp-list{display:grid;grid-template-rows:repeat(4,1fr)}
.persp-item{position:relative;border-bottom:1px solid var(--line-dark);padding:28px 0 0 72px}
.persp-item.active{background:var(--forest-2)}
.persp-item .num{position:absolute;left:32px;top:28px;font-size:6px;color:#9fb39a}
.persp-item h3{font-family:var(--serif);font-weight:400;font-size:20px}
.persp-item p{font-size:7.5px;color:#9fb39a;margin-top:8px}

/* philosophy */
.philosophy{height:800px;background:var(--stone)}
.phil-head em{text-decoration:underline;text-decoration-thickness:1px;text-underline-offset:6px}
.cards{position:absolute;left:120px;top:337px;width:960px;height:363px;display:grid;grid-template-columns:repeat(4,1fr);border-top:1px solid var(--line-light);border-bottom:1px solid var(--line-light)}
.card{position:relative;border-right:1px solid var(--line-light);padding:74px 20px 0}
.card:last-child{border-right:0}
.card h3{font-family:var(--serif);font-weight:400;font-size:22px;line-height:1.05}
.card p{font-size:7.5px;line-height:1.7;color:var(--muted);margin-top:12px}
.card-art{position:absolute;left:20px;bottom:30px;width:150px;height:80px;background:radial-gradient(ellipse at 40% 55%,rgba(111,154,95,.35) 0%,rgba(111,154,95,.08) 60%,rgba(232,232,223,0) 80%)}

/* quote */
.quote{height:586px;background:radial-gradient(ellipse at 62% 45%,#5f9250 0%,#46783a 40%,var(--leaf) 80%);color:#f1f5ec}
.quote blockquote{position:absolute;left:120px;top:165px;font-size:64px;line-height:1.02}
.quote .cite{position:absolute;left:120px;top:458px;color:#b9dca6;font-size:6.5px}

/* team */
.team{height:744px;background:var(--paper)}
.team-visual{position:absolute;left:392px;top:299px;width:358px;height:340px;background:linear-gradient(160deg,#e3eddc 0%,#bcd6ae 60%,#a3c593 100%)}
.team-copy{position:absolute;left:798px;top:489px;width:270px;font-size:9px;line-height:1.8;color:#4d564a}
.team-note{margin-top:14px;border-left:1px solid var(--ink);padding-left:10px;font-size:6.5px;color:var(--muted)}

/* contact */
.contact{height:465px;background:var(--forest);color:#eef2ea}
.contact h2{font-size:76px;line-height:.95}
.contact h2 em{color:var(--mint)}
.field{position:absolute;left:667px;width:413px;height:44px;border-bottom:1px solid var(--line-dark);display:flex;align-items:center}
.field span{width:62px;font-size:6px;letter-spacing:.14em;color:#9fb39a}
.field b{font-weight:400;font-size:10px;color:#6f8a6a}
.send{position:absolute;left:667px;top:300px;width:413px;height:42px;background:var(--mint);color:var(--forest);display:flex;justify-content:space-between;align-items:center;padding:0 18px;font-size:6.5px;letter-spacing:.14em;font-weight:600}

/* footer */
.footer{height:193px;background:var(--mint-pale)}
.footer .brand{position:absolute;left:120px;top:58px;font-size:22px;color:var(--ink)}
.footer .brand small{font-size:12px}
.footer-tag{position:absolute;left:377px;top:60px;font-family:var(--serif);font-size:20px;line-height:1.1}
.footer-links{position:absolute;right:120px;top:56px;text-align:right;font-size:7px;line-height:2.1}
.footer-base{position:absolute;left:120px;right:120px;top:178px;display:flex;font-size:5.5px;letter-spacing:.12em;color:var(--muted)}
.footer-base span:nth-child(2){margin-left:200px}
.footer-base span:last-child{margin-left:auto}
</style>
</head>
<body>

<header class="hero">
  <nav class="nav">
    <div class="brand"><span class="brand-dot"></span><div>HALDEN<small>FORUM</small></div></div>
    <div class="nav-links"><span>PERSPECTIVES</span><span>APPROACH</span><span>PHILOSOPHY</span></div>
    <div class="nav-cta"><span>START A CONVERSATION</span><svg width="12" height="12" viewBox="0 0 12 12"><path d="M1 11L11 1M4 1h7v7" stroke="#eef2ea" fill="none"/></svg></div>
  </nav>
  <div class="abs label" style="left:120px;top:86px;color:#9fb39a">01 &nbsp;&nbsp; Global research &amp; investment</div>
  <div class="abs label" style="left:525px;top:86px;color:#9fb39a">Multiple views. One clear conviction.</div>
  <div class="hero-art" role="img" aria-label="Layered translucent green geometric composition suggesting many viewpoints"></div>
  <div class="abs label" style="left:668px;top:153px;color:#7f9479;font-size:5.5px">Global context</div>
  <div class="abs label" style="left:790px;top:570px;color:#7f9479;font-size:5.5px">Long-term view</div>
  <div class="abs label" style="left:1130px;top:285px;color:#7f9479;font-size:5.5px">Independent</div>
  <h1 class="hero-title serif"><span>See beyond</span><span style="padding-left:75px">a single point</span><span style="padding-left:15px">of <em>view.</em></span></h1>
  <p class="hero-desc">Halden Forum brings distinct research perspectives into focus to support disciplined, long-term investment thinking.</p>
  <div class="hero-btn">EXPLORE OUR<br>PERSPECTIVE<span style="font-size:12px;margin-top:4px">↓</span></div>
</header>

<section class="forum">
  <div class="abs label label-rule" style="left:120px;top:107px;color:var(--muted)">02 &nbsp;&nbsp; The forum</div>
  <div class="abs label" style="left:392px;top:107px;color:var(--muted)">A wider field of view</div>
  <h2 class="abs big-head serif" style="left:392px;top:137px">A forum is stronger when<br>no single view <em>dominates.</em></h2>
  <p class="abs" style="left:703px;top:314px;width:380px;font-size:9px;line-height:1.8;color:#4d564a">We look across regions, disciplines and time horizons. Each perspective tests the others, revealing what holds up when assumptions are challenged.</p>
  <div class="abs link-line" style="left:703px;top:392px;width:377px"><span>READ OUR PHILOSOPHY</span><span>↗</span></div>
  <div class="marquee">Observe<i>+</i>Challenge<i>+</i>Connect</div>
</section>

<section class="perspectives">
  <div class="abs label label-rule" style="left:120px;top:108px;color:#9fb39a">03 &nbsp;&nbsp; Four perspectives</div>
  <h2 class="abs persp-head serif" style="left:392px;top:103px">Conviction becomes<br>clearer when ideas are<br>seen from <em>more than one<br>angle.</em></h2>
  <div class="persp-grid">
    <div class="persp-visual">
      <div class="persp-art" role="img" aria-label="Soft green field where four perspectives converge into conviction">Conviction</div>
      <div class="abs label" style="left:14px;bottom:14px;color:#5f7759;font-size:5.5px">Clarity of outcome</div>
    </div>
    <div class="persp-list">
      <div class="persp-item active"><span class="num">01</span><h3>Global context</h3><p>See ideas within the systems that shape them.</p></div>
      <div class="persp-item"><span class="num">02</span><h3>Structural change</h3><p>Distinguish durable shifts from passing noise.</p></div>
      <div class="persp-item"><span class="num">03</span><h3>Independent research</h3><p>Question consensus before accepting the obvious.</p></div>
      <div class="persp-item"><span class="num">04</span><h3>Long-term discipline</h3><p>Give strong ideas the time required to endure.</p></div>
    </div>
  </div>
</section>

<section class="philosophy">
  <div class="abs label label-rule" style="left:120px;top:108px;color:var(--muted)">04 &nbsp;&nbsp; Investment philosophy</div>
  <div class="abs label" style="left:392px;top:108px;color:var(--muted)">From perspective to conviction</div>
  <h2 class="abs big-head serif phil-head" style="left:392px;top:135px">Ideas are not collected.<br>They are <em>tested.</em></h2>
  <div class="cards">
    <div class="card"><h3>Look beyond the<br>headline.</h3><p>Begin with broad context and patient observation before forming a view.</p>
      <div class="card-art" role="img" aria-label="Small green motif of overlapping views"></div></div>
    <div class="card"><h3>Put assumptions<br>under pressure.</h3><p>Use opposing perspectives to expose weak reasoning and hidden risk.</p>
      <div class="card-art" role="img" aria-label="Small green motif of shapes under pressure"></div></div>
    <div class="card"><h3>Find the structure<br>within change.</h3><p>Connect evidence across disciplines until a coherent thesis emerges.</p>
      <div class="card-art" role="img" aria-label="Small green motif of scattered evidence points"></div></div>
    <div class="card"></div>
  </div>
</section>

<section class="quote">
  <blockquote class="serif">“The goal is not to see the<br>future from one perfect angle.<br>It is to build a view that can<br>withstand many.”</blockquote>
  <div class="label cite">Guiding idea for Halden Forum</div>
</section>

<section class="team">
  <div class="abs label label-rule" style="left:120px;top:111px;color:var(--muted)">05 &nbsp;&nbsp; The team</div>
  <h2 class="abs big-head serif" style="left:392px;top:134px">Built by people who value<br><em>independent thought.</em></h2>
  <div class="team-visual" role="img" aria-label="Team photography area in soft green tones">
    <div class="abs label" style="left:16px;bottom:12px;color:#6d8a62;font-size:5.5px">Team photography</div>
  </div>
  <div class="team-copy">Halden Forum brings together complementary experience and distinct viewpoints around a shared commitment to rigorous research.
    <div class="team-note">Team names, roles and biographies will be added when supplied.</div>
  </div>
  <div class="abs link-line" style="left:798px;top:605px;width:282px"><span>MEET THE TEAM</span><span>↗</span></div>
</section>

<section class="contact">
  <div class="abs label" style="left:120px;top:107px;color:#9fb39a">Start a conversation</div>
  <h2 class="abs serif" style="left:120px;top:150px">Bring another<br><em>perspective.</em></h2>
  <p class="abs" style="left:120px;top:315px;width:270px;font-size:9px;line-height:1.7;color:#b5c2b0">For research, investment or partnership enquiries, connect with Halden Forum.</p>
  <div class="field" style="top:110px"><span>NAME</span><b>Your name</b></div>
  <div class="field" style="top:158px"><span>EMAIL</span><b>you@company.com</b></div>
  <div class="field" style="top:206px"><span>MESSAGE</span><b>How can we help?</b></div>
  <div class="send"><span>SEND ENQUIRY</span><span style="font-size:11px">↗</span></div>
</section>

<footer class="footer">
  <div class="brand"><span class="brand-dot"></span><div>HALDEN<small>FORUM</small></div></div>
  <div class="footer-tag">Global research.<br>Independent perspective.</div>
  <div class="footer-links">Perspectives<br>Philosophy<br>Team<br>Contact</div>
  <div class="footer-base"><span>© 2025 HALDEN FORUM</span><span>WEBSITE CONCEPT</span><span>BACK TO TOP ↑</span></div>
</footer>

</body>
</html>
```